Web design for trailer business

We are a digital marketing company and are rebuilding a website for an established trailer business. Their current website is: https://www.dunlacktrailers.com.au/
They want a new website designed with a similar style to a competitor: https://www.grevikstrailers.com.au/
The three main page styles that need to be done are:
Home page: https://www.grevikstrailers.com.au/
Category page: https://www.grevikstrailers.com.au/machinery-trailers/
Product view page: https://www.grevikstrailers.com.au/8-x-5-tandem-plant-trailer/
Their colour scheme is actually changing to orange and blue instead of yellow and blue. The colours are the ones in the 'Certified By' section of the footer, with the image of VEP International.
Number of Pages Required
3 page
Look and feel
Each slider illustrates characteristics of the customer's brand and the style your logo design should communicate.

```html
<!DOCTYPE html>
<html lang="en">
<head>
<meta charset="utf-8">
<title>Korvane Trailers – Home</title>
<link href="https://fonts.googleapis.com/css2?family=Open+Sans:wght@400;600;700&family=Roboto:wght@400;500;700;900&display=swap" rel="stylesheet">
<style>
:root{
  --blue:#1d5fae;
  --blue-dark:#14467f;
  --orange:#f7941d;
  --orange-dark:#e07c0a;
  --ink:#333;
  --muted:#777;
  --line:#e3e3e3;
  --footer:#1f1f1f;
  --footer-bar:#151515;
  --white:#fff;
}
*{box-sizing:border-box;margin:0;padding:0}
html,body{width:1200px;height:2876px;overflow:hidden}
body{font-family:"Open Sans",Arial,sans-serif;color:var(--ink);background:#fff;font-size:13px;line-height:1.6}
h1,h2,h3,h4{font-family:"Roboto",Arial,sans-serif}
.wrap{width:980px;margin:0 auto}

/* header */
.topbar{height:72px;display:flex;align-items:center}
.topbar .wrap{display:flex;align-items:center;justify-content:space-between}
.brand{display:flex;align-items:center;gap:10px;font-family:"Roboto",sans-serif;font-weight:700;font-size:18px;color:var(--blue)}
.brand i{width:22px;height:22px;border-radius:50%;background:var(--orange);display:block}
.contacts{display:flex;gap:34px;align-items:center}
.contact{display:flex;gap:8px;align-items:center;font-size:10px;line-height:1.3}
.contact svg{width:24px;height:24px}
.contact b{display:block;color:var(--ink);font-size:10px;letter-spacing:.5px}
.contact span{color:var(--muted)}
.btn-orange{background:var(--orange);color:#fff;font-weight:700;font-size:11px;padding:6px 16px;border-radius:2px;font-family:"Roboto",sans-serif;text-transform:uppercase}
.nav{height:32px;background:var(--blue)}
.nav ul{list-style:none;display:flex;gap:26px;height:32px;align-items:center;font-family:"Roboto",sans-serif;font-size:10px;font-weight:500;color:#fff;text-transform:uppercase}

/* hero */
.hero{position:relative;height:396px;background:linear-gradient(180deg,#6d7a86 0%,#a8b1b9 45%,#8c8f8c 70%,#6e6a62 100%)}
.hero-title{position:absolute;top:150px;width:100%;text-align:center;color:#fff;font-family:"Roboto",sans-serif;font-weight:900;font-size:38px;line-height:1.1;letter-spacing:1px}
.hero-sub{position:absolute;top:200px;width:100%;text-align:center;color:#fff;font-size:11px}
.hero .btn-blue{position:absolute;top:272px;left:50%;transform:translateX(-50%);background:var(--blue);color:#fff;font-size:10px;font-weight:700;padding:6px 16px;font-family:"Roboto",sans-serif}
.hero-arrow{position:absolute;top:186px;width:26px;height:26px;background:rgba(255,255,255,.85);display:flex;align-items:center;justify-content:center}
.hero-arrow.left{left:14px}.hero-arrow.right{right:14px}

/* intro */
.intro{height:488px;padding-top:64px}
.intro .wrap{display:flex;justify-content:space-between}
.intro-text{width:480px;margin-left:12px}
.intro-text h2{font-size:18px;font-weight:700;color:#222;margin-bottom:14px}
.intro-text p{font-size:10.5px;color:var(--muted);margin-bottom:12px;line-height:1.75}
.quote{width:222px;border:1px solid var(--line);box-shadow:0 2px 8px rgba(0,0,0,.08);padding:16px 16px 20px;margin-top:-4px;height:380px;margin-right:20px}
.quote h3{font-size:11px;font-weight:700;text-transform:uppercase;margin-bottom:18px;border-bottom:2px solid var(--orange);padding-bottom:6px;display:inline-block}
.quote .field{height:30px;border:1px solid var(--line);margin-bottom:14px;font-size:9px;color:#999;padding:7px 10px}
.quote .field.area{height:56px}
.quote .submit{background:var(--orange);color:#fff;font-size:9px;font-weight:700;display:inline-block;padding:7px 14px;font-family:"Roboto",sans-serif;margin-top:6px}

/* trailer grid */
.grid{display:grid;grid-template-columns:repeat(4,1fr);gap:6px;padding:0 2px;height:564px}
.tile{position:relative;height:184px}
.tile .photo{position:absolute;inset:0}
.tile .label{position:absolute;left:0;right:0;bottom:0;height:22px;background:var(--blue);color:#fff;text-align:center;font-family:"Roboto",sans-serif;font-size:9.5px;font-weight:700;line-height:22px;text-transform:uppercase}
.p1{background:linear-gradient(160deg,#e9ecef,#b9c0c6)}
.p2{background:linear-gradient(160deg,#c9d3da,#6d7a85)}
.p3{background:linear-gradient(160deg,#dfe4e8,#8d99a3)}
.p4{background:linear-gradient(160deg,#a8c3d9,#7f8a7c)}
.p5{background:linear-gradient(160deg,#d7dadc,#5f6a73)}
.p6{background:linear-gradient(160deg,#e3e6e8,#a1a9af)}
.p7{background:linear-gradient(160deg,#cfe2f3,#2f6fb3)}
.p8{background:linear-gradient(160deg,#e6e8ea,#9aa3aa)}
.p9{background:linear-gradient(160deg,#eef0f1,#b5bcc1)}
.p10{background:linear-gradient(160deg,#bfc5c9,#4d5358)}
.p11{background:linear-gradient(160deg,#d8dde0,#8a949b)}
.p12{background:linear-gradient(160deg,#f6e9a8,#e0b82a)}

/* services */
.services{height:328px;background:linear-gradient(180deg,var(--blue) 0%,var(--blue-dark) 100%);text-align:center;padding-top:80px}
.services h2{color:#fff;font-size:13px;font-weight:700;text-transform:uppercase}
.services .rule{width:40px;height:2px;background:var(--orange);margin:6px auto 22px}
.service-cards{display:flex;justify-content:center;gap:20px}
.service{width:176px;height:82px;background:#fff;display:flex;gap:10px;padding:14px;text-align:left}
.service .ico{width:30px;height:30px;border-radius:50%;background:var(--orange);flex:none;display:flex;align-items:center;justify-content:center}
.service h4{font-size:9.5px;font-weight:700;color:#222}
.service p{font-size:8px;color:var(--muted);line-height:1.45}

/* about */
.about{height:300px;padding-top:40px}
.about .wrap{display:flex;gap:60px;margin-left:240px;width:760px}
.video{width:290px;height:210px;background:linear-gradient(160deg,#3a4450,#97a3ad 60%,#c9cfd4);position:relative;flex:none}
.video .play{position:absolute;left:50%;top:50%;width:44px;height:44px;margin:-22px;border-radius:50%;background:rgba(255,255,255,.9);display:flex;align-items:center;justify-content:center}
.about-text{width:380px}
.about-text h2{font-size:14px;font-weight:700;text-transform:uppercase}
.about-text .rule{width:36px;height:2px;background:var(--orange);margin:6px 0 12px}
.about-text p{font-size:9.5px;color:var(--muted);line-height:1.6;margin-bottom:8px}
.about-text .more{color:var(--orange);font-size:10px;font-weight:700}

/* testimonials */
.testimonials{height:360px;background:linear-gradient(180deg,var(--orange) 0%,var(--orange-dark) 100%);text-align:center;padding-top:36px;color:#fff}
.testimonials h2{font-size:13px;font-weight:700;text-transform:uppercase}
.testimonials .rule{width:40px;height:2px;background:#fff;margin:6px auto 26px}
.quotes{display:flex;justify-content:center;gap:40px}
.tcard{width:230px}
.avatar{width:40px;height:40px;border-radius:50%;background:linear-gradient(160deg,#f4c47c,#b9701c);margin:0 auto 8px}
.tcard h4{font-size:10px;font-weight:700}
.tcard p{font-size:8.5px;line-height:1.55;margin-top:6px;opacity:.95}
.dots{display:flex;gap:6px;justify-content:center;margin-top:24px}
.dots i{width:7px;height:7px;border-radius:50%;background:rgba(255,255,255,.5)}
.dots i:first-child{background:#fff}

/* footer */
.footer{height:300px;background:var(--footer);color:#bbb;padding-top:36px}
.footer .wrap{display:flex;gap:40px;width:1000px}
.fcol{width:220px;font-size:9px;line-height:1.5}
.fcol.narrow{width:140px}
.fcol h4{color:#fff;font-size:10px;font-weight:700;text-transform:uppercase;margin-bottom:12px;display:flex;align-items:center;gap:6px}
.fcol h4::before{content:"";width:6px;height:6px;background:var(--orange);display:block}
.frow{display:flex;gap:8px;margin-bottom:10px}
.frow svg{width:12px;height:12px;flex:none;margin-top:1px}
.flist{list-style:none}
.flist li{margin-bottom:4px}
.badges{display:flex;gap:8px;flex-wrap:wrap;width:150px}
.badge{width:40px;height:40px;background:var(--orange);border-radius:50%}
.badge.sq{border-radius:2px;background:var(--blue)}
.badge.gr{border-radius:2px;background:#4e9a3a;width:70px}
.bottom{height:36px;background:var(--footer-bar);color:#888;font-size:8.5px}
.bottom .wrap{display:flex;justify-content:space-between;align-items:center;height:36px}
</style>
</head>
<body>

<header class="topbar">
  <div class="wrap">
    <div class="brand"><i></i>Korvane Trailers</div>
    <div class="contacts">
      <div class="contact">
        <svg viewBox="0 0 24 24"><circle cx="12" cy="12" r="12" fill="#1d5fae"/><path d="M8.5 7l2 2-1.2 1.4c.7 1.5 1.8 2.6 3.3 3.3L14 12.5l2 2-1.3 1.8C10.6 16 8 13.4 7.7 8.3z" fill="#fff"/></svg>
        <div><b>KELMSWOOD</b><span>(03) 9000 4812</span></div>
      </div>
      <div class="contact">
        <svg viewBox="0 0 24 24"><circle cx="12" cy="12" r="12" fill="#1d5fae"/><path d="M8.5 7l2 2-1.2 1.4c.7 1.5 1.8 2.6 3.3 3.3L14 12.5l2 2-1.3 1.8C10.6 16 8 13.4 7.7 8.3z" fill="#fff"/></svg>
        <div><b>HARLOW PARK</b><span>(03) 9000 7365</span></div>
      </div>
      <div class="contact">
        <svg viewBox="0 0 24 24"><circle cx="12" cy="12" r="12" fill="#1d5fae"/><rect x="6.5" y="8" width="11" height="8" fill="none" stroke="#fff" stroke-width="1.3"/><path d="M6.5 8l5.5 4.5L17.5 8" fill="none" stroke="#fff" stroke-width="1.3"/></svg>
        <div><b>CONTACT US</b><span>hello@korvanetrailers.com.au</span></div>
      </div>
    </div>
    <span class="btn-orange">Get a Quote</span>
  </div>
</header>

<nav class="nav">
  <div class="wrap">
    <ul><li>Home</li><li>About Us</li><li>Trailers</li><li>Trailer Parts</li><li>Service</li><li>Request Quote</li><li>Contact Us</li></ul>
  </div>
</nav>

<section class="hero" role="img" aria-label="Photo of a black tandem plant trailer parked in a trailer yard">
  <div class="hero-title">REALIABLE LOGISTICS SERVICES</div>
  <div class="hero-sub">Quality trailers built tough for every job, load and road across the state</div>
  <span class="btn-blue">READ MORE</span>
  <div class="hero-arrow left"><svg width="10" height="10" viewBox="0 0 10 10"><path d="M7 1L3 5l4 4" stroke="#333" stroke-width="1.6" fill="none"/></svg></div>
  <div class="hero-arrow right"><svg width="10" height="10" viewBox="0 0 10 10"><path d="M3 1l4 4-4 4" stroke="#333" stroke-width="1.6" fill="none"/></svg></div>
</section>

<section class="intro">
  <div class="wrap">
    <div class="intro-text">
      <h2>TRAILERS FOR SALE</h2>
      <p>Korvane Trailers is a family owned business that has been building quality trailers for many years. We design and manufacture every trailer in our own workshop using strong steel, tested parts and careful welding, so each unit is ready for heavy daily use on farms, building sites and weekend trips alike.</p>
      <p>From small box trailers to large plant machinery trailers, our team can build a standard model or a custom unit to suit your exact needs and budget.</p>
      <p>Visit one of our two yards to see our full range in person, talk with our friendly staff and get honest advice on the right trailer for the work you do every day.</p>
    </div>
    <form class="quote">
      <h3>Get a Quick Quote</h3>
      <div class="field">Full Name</div>
      <div class="field">Email</div>
      <div class="field">Phone</div>
      <div class="field">Trailer Type</div>
      <div class="field area">Your Message</div>
      <span class="submit">SUBMIT YOUR QUOTE</span>
    </form>
  </div>
</section>

<section class="grid">
  <div class="tile"><div class="photo p1" role="img" aria-label="Box trailer photo"></div><div class="label">Box Trailers</div></div>
  <div class="tile"><div class="photo p2" role="img" aria-label="Cage trailer photo"></div><div class="label">Cage Trailers</div></div>
  <div class="tile"><div class="photo p3" role="img" aria-label="Custom built trailer photo"></div><div class="label">Custom Built Trailers</div></div>
  <div class="tile"><div class="photo p4" role="img" aria-label="Car trailer photo"></div><div class="label">Car Trailers</div></div>
  <div class="tile"><div class="photo p5" role="img" aria-label="Flat bed trailer photo"></div><div class="label">Flat Bed Trailers</div></div>
  <div class="tile"><div class="photo p6" role="img" aria-label="Flat top trailer photo"></div><div class="label">Flat Top Trailers</div></div>
  <div class="tile"><div class="photo p7" role="img" aria-label="Blue enclosed trailer photo"></div><div class="label">Enclosed Trailers</div></div>
  <div class="tile"><div class="photo p8" role="img" aria-label="Tandem trailer photo"></div><div class="label">Tandem Trailers</div></div>
  <div class="tile"><div class="photo p9" role="img" aria-label="Hydraulic tipper trailer photo"></div><div class="label">Hydraulic Tipper Trailers</div></div>
  <div class="tile"><div class="photo p10" role="img" aria-label="Van enclosed trailer photo"></div><div class="label">Van Enclosed Trailers</div></div>
  <div class="tile"><div class="photo p11" role="img" aria-label="Plant machinery trailer photo"></div><div class="label">Plant Machinery Trailers</div></div>
  <div class="tile"><div class="photo p12" role="img" aria-label="Yellow motorbike trailer photo"></div><div class="label">Motorbike Trailers</div></div>
</section>

<section class="services">
  <h2>Our Services</h2>
  <div class="rule"></div>
  <div class="service-cards">
    <div class="service">
      <div class="ico"><svg width="14" height="14" viewBox="0 0 14 14"><path d="M2 7l3 3 7-7" stroke="#fff" stroke-width="2" fill="none"/></svg></div>
      <div><h4>Trailer Parts</h4><p>Wheels, lights, hitches and spares in stock for fast fitting.</p></div>
    </div>
    <div class="service">
      <div class="ico"><svg width="14" height="14" viewBox="0 0 14 14"><path d="M2 7l3 3 7-7" stroke="#fff" stroke-width="2" fill="none"/></svg></div>
      <div><h4>Repair and Maintenance</h4><p>Servicing, brakes and welding done by skilled staff.</p></div>
    </div>
    <div class="service">
      <div class="ico"><svg width="14" height="14" viewBox="0 0 14 14"><path d="M2 7l3 3 7-7" stroke="#fff" stroke-width="2" fill="none"/></svg></div>
      <div><h4>Custom Trailers</h4><p>Built to your size, load and use from the ground up.</p></div>
    </div>
  </div>
</section>

<section class="about">
  <div class="wrap">
    <div class="video" role="img" aria-label="Video still of trailers in the workshop">
      <div class="play"><svg width="16" height="16" viewBox="0 0 16 16"><path d="M5 3l8 5-8 5z" fill="#1d5fae"/></svg></div>
    </div>
    <div class="about-text">
      <h2>About Us</h2>
      <div class="rule"></div>
      <p>At Korvane Trailers we are committed to making the best trailers for our customers. Every trailer is built in house by a team that cares about strength, finish and long life on the road.</p>
      <p>Established over twenty years ago, we have grown from a small shed into two busy yards. We still treat every customer like a neighbour and stand behind each trailer we sell.</p>
      <p>Our range covers box, cage, car, tipper and plant trailers, plus custom builds for trade and farm work.</p>
      <span class="more">READ MORE</span>
    </div>
  </div>
</section>

<section class="testimonials">
  <h2>Client Testimonials</h2>
  <div class="rule"></div>
  <div class="quotes">
    <div class="tcard"><div class="avatar" role="img" aria-label="Customer portrait"></div><h4>Mark T.</h4><p>Great service and a solid trailer. The team helped me pick the right size and it has worked hard every day.</p></div>
    <div class="tcard"><div class="avatar" role="img" aria-label="Customer portrait"></div><h4>Sarah L.</h4><p>Friendly staff, fair price and quick delivery. I would happily buy my next trailer here again.</p></div>
    <div class="tcard"><div class="avatar" role="img" aria-label="Customer portrait"></div><h4>James P.</h4><p>My custom plant trailer was built exactly to plan. Strong welds and a very clean finish.</p></div>
  </div>
  <div class="dots"><i></i><i></i><i></i></div>
</section>

<footer class="footer">
  <div class="wrap">
    <div class="fcol">
      <h4>Korvane Trailers Kelmswood</h4>
      <div class="frow"><svg viewBox="0 0 12 12"><path d="M6 1a3.5 3.5 0 0 0-3.5 3.5C2.5 7 6 11 6 11s3.5-4 3.5-6.5A3.5 3.5 0 0 0 6 1z" fill="#f7941d"/></svg><span>14 Foundry Road, Kelmswood VIC 3170</span></div>
      <div class="frow"><svg viewBox="0 0 12 12"><path d="M3 1.5l2 2-1 1.2c.6 1.3 1.6 2.3 2.9 2.9L8 6.5l2 2-1.2 1.5C5 9.8 2.2 7 1.9 2.7z" fill="#f7941d"/></svg><span>(03) 9000 4812</span></div>
      <div class="frow"><svg viewBox="0 0 12 12"><rect x="1" y="3" width="10" height="7" fill="none" stroke="#f7941d"/><path d="M1 3l5 4 5-4" fill="none" stroke="#f7941d"/></svg><span>hello@korvanetrailers.com.au</span></div>
    </div>
    <div class="fcol">
      <h4>Korvane Trailers Harlow Park</h4>
      <div class="frow"><svg viewBox="0 0 12 12"><path d="M6 1a3.5 3.5 0 0 0-3.5 3.5C2.5 7 6 11 6 11s3.5-4 3.5-6.5A3.5 3.5 0 0 0 6 1z" fill="#f7941d"/></svg><span>7 Carrow Street, Harlow Park VIC 3153</span></div>
      <div class="frow"><svg viewBox="0 0 12 12"><path d="M3 1.5l2 2-1 1.2c.6 1.3 1.6 2.3 2.9 2.9L8 6.5l2 2-1.2 1.5C5 9.8 2.2 7 1.9 2.7z" fill="#f7941d"/></svg><span>(03) 9000 7365</span></div>
      <div class="frow"><svg viewBox="0 0 12 12"><rect x="1" y="3" width="10" height="7" fill="none" stroke="#f7941d"/><path d="M1 3l5 4 5-4" fill="none" stroke="#f7941d"/></svg><span>hello@korvanetrailers.com.au</span></div>
    </div>
    <div class="fcol narrow">
      <h4>Trailers</h4>
      <ul class="flist">
        <li>Box Trailers</li><li>Cage Trailers</li><li>Custom Built Trailers</li><li>Car Trailers</li><li>Flat Bed Trailers</li><li>Flat Top Trailers</li><li>Tipper Trailers</li><li>Plant Trailers</li><li>Motorbike Trailers</li>
      </ul>
    </div>
    <div class="fcol">
      <h4>Certified By</h4>
      <div class="badges">
        <div class="badge"></div><div class="badge sq"></div><div class="badge gr"></div>
      </div>
    </div>
  </div>
</footer>
<div class="bottom">
  <div class="wrap"><span>© 2024 Korvane Trailers. All rights reserved.</span><span>Privacy Policy · Terms</span></div>
</div>

</body>
</html>
```